Stonebay Towing Business Card

Towing
Accident towing
Mechanical breakdown
Insurance, salvage and recovery
4wd off road towing
Light & Heavy towing
8347 2516
24 hour business 7 days

Logo can be whole size on front

Industry/Entity Type

Towing/ transport

Contact Information for Business Card

The above

```html
<!DOCTYPE html>
<html lang="en">
<head>
<meta charset="utf-8">
<title>Stonebay Towing Business Card</title>
<link href="https://fonts.googleapis.com/css2?family=Montserrat:wght@400;500;700;800&display=swap" rel="stylesheet">
<style>
  :root {
    --stage: #a4a4a4;
    --ink: #161616;
    --red: #d11f2a;
    --paper: #f2f1f5;
    --text-dark: #1d1d1d;
    --white: #ffffff;
  }
  * { margin: 0; padding: 0; box-sizing: border-box; }
  html, body { width: 1200px; height: 1200px; overflow: hidden; }
  body {
    background: var(--stage);
    font-family: "Montserrat", sans-serif;
    position: relative;
  }
  .card {
    position: absolute;
    left: 219px;
    width: 763px;
    border-radius: 22px;
    overflow: hidden;
  }
  .card-front {
    top: 161px;
    height: 422px;
    background: var(--ink);
    display: flex;
    align-items: center;
    justify-content: center;
  }
  .front-brand {
    color: var(--red);
    font-weight: 800;
    font-size: 72px;
    letter-spacing: -1px;
    margin-top: -20px;
  }
  .card-back {
    top: 619px;
    height: 420px;
    background: var(--paper);
  }
  .back-wave { position: absolute; inset: 0; width: 763px; height: 420px; }
  .holder { position: absolute; left: 32px; top: 40px; }
  .holder-name {
    color: var(--red);
    font-weight: 700;
    font-size: 26px;
    letter-spacing: 0.5px;
    line-height: 1;
  }
  .holder-role {
    color: var(--text-dark);
    font-size: 18px;
    font-weight: 500;
    margin-top: 10px;
  }
  .contacts { position: absolute; left: 32px; top: 121px; list-style: none; }
  .contacts li {
    display: flex;
    align-items: center;
    gap: 8px;
    font-size: 20px;
    color: var(--text-dark);
    height: 29.5px;
  }
  .contacts svg { width: 18px; height: 18px; flex: none; }
  .back-brand {
    position: absolute;
    right: 36px;
    top: 58px;
    color: var(--red);
    font-weight: 800;
    font-size: 32px;
    letter-spacing: -0.5px;
  }
  .services {
    position: absolute;
    right: 32px;
    top: 203px;
    list-style: none;
    text-align: right;
  }
  .services li {
    color: var(--white);
    font-size: 19px;
    font-weight: 500;
    height: 27px;
    line-height: 27px;
  }
  .services li::after {
    content: "";
    display: inline-block;
    width: 7px; height: 7px;
    border-radius: 50%;
    background: var(--red);
    margin-left: 10px;
    vertical-align: middle;
  }
  .hotline {
    position: absolute;
    left: 30px;
    bottom: 27px;
    display: flex;
    align-items: center;
    gap: 6px;
    color: var(--white);
    font-weight: 800;
    font-size: 22px;
    letter-spacing: 2px;
  }
  .hotline-icon {
    width: 20px; height: 20px;
    background: var(--red);
    border-radius: 3px;
    display: flex; align-items: center; justify-content: center;
  }
  .hotline-icon svg { width: 14px; height: 14px; }
</style>
</head>
<body>
  <section class="card card-front">
    <div class="front-brand">Stonebay Towing</div>
  </section>

  <section class="card card-back">
    <svg class="back-wave" viewBox="0 0 763 420" aria-hidden="true">
      <path d="M0 278 C120 332 260 322 400 262 C540 202 640 178 763 198 V420 H0 Z" fill="#161616" stroke="#f2f1f5" stroke-width="6"/>
      <path d="M0 232 C80 300 230 310 380 250 C520 195 640 136 763 176 V196 C640 170 540 196 400 256 C260 314 110 318 0 266 Z" fill="#d11f2a"/>
    </svg>

    <div class="holder">
      <div class="holder-name">MARLA QUINLAN</div>
      <div class="holder-role">Owner</div>
    </div>

    <ul class="contacts">
      <li>
        <svg viewBox="0 0 24 24"><path fill="#d11f2a" d="M3 9c0-3 4-5 9-5s9 2 9 5v2h-5V9H8v2H3zM6 12h12l2 8H4z"/></svg>
        8347 2516
      </li>
      <li>
        <svg viewBox="0 0 24 24"><rect x="6" y="2" width="12" height="20" rx="2" fill="none" stroke="#d11f2a" stroke-width="2"/><circle cx="12" cy="18" r="1.2" fill="#d11f2a"/></svg>
        (415) 555-0148
      </li>
      <li>
        <svg viewBox="0 0 24 24"><rect x="2" y="5" width="20" height="14" fill="#d11f2a"/><path d="M2 5l10 8 10-8" fill="none" stroke="#f2f1f5" stroke-width="1.6"/></svg>
        info@stonebaytowing.com
      </li>
    </ul>

    <div class="back-brand">Stonebay Towing</div>

    <ul class="services">
      <li>Towing</li>
      <li>Accident towing</li>
      <li>Mechanical breakdown</li>
      <li>Insurance, salvage and recovery</li>
      <li>4wd off road towing</li>
      <li>Light &amp; Heavy towing</li>
      <li>24 hour business 7 days</li>
    </ul>

    <div class="hotline">
      <span class="hotline-icon">
        <svg viewBox="0 0 24 24"><path fill="#ffffff" d="M3 9c0-3 4-5 9-5s9 2 9 5v2h-5V9H8v2H3zM6 12h12l2 8H4z"/></svg>
      </span>
      8347 2516
    </div>
  </section>
</body>
</html>
```